Business broker needs designs for business card, letterhead and email signature

I require the following items:
- business cards
- letterhead
- email signature

My company is a Business Broker company that specialises in business sales across various industries. The company has branches in four areas and each area has its own logo and website. Initially for the submission I am happy to inspect 1 design and 1 layout for quillharborgroup but the winner will need to complete a design for each area.

The four areas are:
1. quillharborgroup
2. tealridgefuelsales
3. orbvalechainsales
4. pondgrovegrocerdeals

I would like one design for each of the above items for each area. In each design, there should be one prominent logo and then the remaining three should also be included, for eg, the letterhead for the quillharborgrp area would have the quillharborgrp logo featuring prominently, somewhere at the top perhaps and the logos of the other three areas would be smaller and perhaps at the bottom, down the side, etc.

For the business cards, one prominent logo should feature on one side with the remaining three logos on the reverse.

The overall objective is for each item to look like it belongs to one family . I need all the source files as I may add new industries moving forward.

Target Market(s)

My company targets business minded people looking to increase wealth,. make an investment or migrate to Australia. People who busy and are looking for efficient and professional service in securing their next business venture.

Industry/Entity Type

Business

Font styles to use
Serif
Sans Serif

Requirements
Must have
• I want something professional and corporate looking, not something cartoony or playful. I am happy for you to be creative.

```html
<!DOCTYPE html>
<html lang="en">
<head>
<meta charset="utf-8">
<title>Email Signatures – quillharborgroup</title>
<link rel="stylesheet" href="https://fonts.googleapis.com/css2?family=Montserrat:wght@400;500;600&display=swap">
<style>
  :root {
    --brand-red: #c8102e;
    --brand-ink: #333e48;
    --text-dark: #2b2b2b;
    --paper: #ffffff;
  }
  * { margin: 0; padding: 0; box-sizing: border-box; }
  html, body { width: 1200px; height: 857px; overflow: hidden; background: var(--paper); }
  body { font-family: "Montserrat", Arial, sans-serif; color: var(--text-dark); }
  .canvas { position: relative; width: 1200px; height: 857px; }

  .abs { position: absolute; white-space: nowrap; }
  .divider { position: absolute; width: 4px; background: var(--brand-red); }

  .name { font-size: 24px; font-weight: 500; color: var(--brand-red); line-height: 1; letter-spacing: 0.2px; }
  .role { font-size: 16.5px; font-weight: 500; color: var(--text-dark); line-height: 1; }
  .line { font-size: 14.5px; font-weight: 500; color: var(--text-dark); line-height: 20px; }
  .web { font-size: 14.5px; font-weight: 500; color: var(--brand-red); line-height: 1; }

  .social { display: flex; gap: 7px; }
  .social span { display: block; width: 17px; height: 16px; background: var(--brand-red); }

  .emblem { position: absolute; border-radius: 50%; background: var(--brand-ink); }

  .wordmark { display: flex; align-items: center; gap: 9px; }
  .wordmark .mark { width: 28px; height: 28px; background: var(--brand-ink); }
  .wordmark .label { font-size: 24px; font-weight: 600; color: var(--brand-ink); line-height: 1; letter-spacing: -0.3px; }

  .contact { display: grid; grid-template-columns: 64px auto; row-gap: 6px; font-size: 15.5px; font-weight: 500; line-height: 18px; }
  .contact dt { color: var(--brand-red); }
  .contact dd { color: var(--text-dark); }
</style>
</head>
<body>
<main class="canvas">

  <section class="signature signature-compact">
    <div class="abs name" style="right:881px; top:121px;">DANIEL REYES</div>
    <div class="abs role" style="right:881px; top:146px;">CEO &amp; President</div>
    <div class="divider" style="left:346px; top:121px; height:94px;"></div>
    <div class="abs line" style="left:374px; top:117px;">Level 12, Harbor Point,<br>88 Kent Lane, Sydney NSW 2000</div>
    <div class="abs web" style="left:374px; top:175px;">www.quillharborgroup.com.au</div>
    <div class="abs social" style="left:374px; top:199px;"><span></span><span></span><span></span></div>
  </section>

  <section class="signature signature-emblem">
    <div class="emblem" style="left:222px; top:337px; width:90px; height:90px;" aria-label="quillharborgroup emblem"></div>
    <div class="divider" style="left:346px; top:335px; height:159px;"></div>
    <div class="abs name" style="left:374px; top:332px;">DANIEL REYES</div>
    <div class="abs role" style="left:374px; top:358px;">CEO &amp; President</div>
    <div class="abs line" style="left:374px; top:392px;">Level 12, Harbor Point,<br>88 Kent Lane, Sydney NSW 2000</div>
    <div class="abs web" style="left:374px; top:447px;">quillharborgroup.com.au</div>
    <div class="abs social" style="left:374px; top:477px;"><span></span><span></span><span></span></div>
  </section>

  <section class="signature signature-full">
    <div class="abs name" style="left:146px; top:612px;">DANIEL REYES</div>
    <div class="abs role" style="left:146px; top:639px;">CEO &amp; President</div>
    <div class="divider" style="left:350px; top:614px; height:187px;"></div>
    <div class="abs wordmark" style="left:366px; top:616px;">
      <span class="mark"></span><span class="label">quillharborgroup</span>
    </div>
    <div class="abs line" style="left:369px; top:664px;">Level 12, Harbor Point, 88 Kent Lane, Sydney NSW 2000</div>
    <dl class="abs contact" style="left:369px; top:699px;">
      <dt>Phone:</dt><dd>1300 555 218</dd>
      <dt>Email:</dt><dd>info@quillharborgroup.com.au</dd>
      <dt>Web:</dt><dd>quillharborgroup.com.au</dd>
    </dl>
    <div class="abs social" style="left:370px; top:784px;"><span></span><span></span><span></span></div>
  </section>

</main>
</body>
</html>
```